A4 Childcare Spring Special Flyer

Crestwell Learning is a registered training organisation (RTO) Toid No. 47318, based in Blackburn, Victoria. We are a market leader in Professional development courses both accredited and non accredited, in order for you to maintain currency in your profession.

We need a flyer for a childcare specific spring special. The special is to offer a $50 VOLM gift card and 50% of your second training session. Conditions apply*

The training sessions available are the NEW childcare specific course: HLTAID004 Provide an emergency first aid response in an education and care setting and HLTAID003 Provide First Aid, HLTAID001 Provide Cardiopulmonary Resuscitation (CPR), 22024VIC Course in emergency management of asthma in the workplace
and 22099VIC Course in First Aid Management of Anaphylaxis.
We provide a flexible, cost effective and reliable service.
We have training locations available in Blackburn, Preston, Narre Warren and Mornington and can also provide onsite training.

We can also provide education and PRIVOS regulation consultation to the childcare provider.

Must use company logo, include phone number: (03) 5127 6481, website: www.crestwelllearning.com.au, email: marapenn@crestwelllearning.com.au

(Note that a letter with more detail will be attached with this flyer, therefore, with that in mind; use that information as desired).

The final product should be as childcare like as possible whilst also keeping our company colors (same as logo). We would also like for this flyer to stand out and be appealing to the recipient as this flyer is to gain potential clients, with emphasis on the HLTAID004 Course
Updates

Just need to update the qualifications: In the design brief I mentioned that the course; HLTAID001 Provide CPR and Asthma & Anaphyalxis.. Can this please be changed to HLTAID001 Provide Cardiopulmonary Resuscitation (CPR) And 22024VIC Course in emergency management of asthma in the workplace And 22099VIC Course in First Aid Management of Anaphylaxis (They are all singular courses) Apoligies!

Target Market(s)

Childcare centres, Out of school hours providers, pre-schools

Industry/Entity Type

Childcare

Font styles to use
Decorative

Colors
ffcf3e
f37123
faa54b

Requirements
Must have
• Company Logo
phone number
website
email
Registered Training Organisation
TOID: 47318

```html
<!DOCTYPE html>
<html lang="en">
<head>
<meta charset="utf-8">
<title>Crestwell Learning – Childcare Spring Special</title>
<link rel="stylesheet" href="https://fonts.googleapis.com/css2?family=Alfa+Slab+One&family=Didact+Gothic&family=Oswald:wght@500;600&family=Roboto:wght@700&display=swap">
<style>
  :root {
    --yellow: #ffcf3e;
    --orange: #f37123;
    --light-orange: #faa54b;
    --red-orange: #ef5a2a;
    --deep-orange: #f0892f;
    --tagline: #fcd20f;
    --ink: #2b2b2b;
    --paper: #ffffff;
    --backdrop: #ece8e2;
  }
  * { margin: 0; padding: 0; box-sizing: border-box; }
  html, body { width: 1044px; height: 1200px; overflow: hidden; }
  body { background: var(--backdrop); position: relative; }

  .flyer {
    position: absolute; left: 96px; top: 0;
    width: 870px; height: 1227px;
    background: var(--paper);
    transform: scale(0.978); transform-origin: top left;
    font-family: "Didact Gothic", sans-serif; color: var(--ink);
  }

  .title-art {
    position: absolute; left: 52px; top: 44px;
    width: 452px; height: 182px;
    background: linear-gradient(100deg, #f6a25a, #8fc7e6 30%, #ef8a7c 60%, #f5d66a 90%);
    border-radius: 8px;
  }

  .brand { position: absolute; left: 690px; top: 32px; width: 150px; text-align: center; }
  .brand-dot { width: 96px; height: 96px; border-radius: 50%; background: var(--orange); margin: 8px auto 40px; }
  .brand-name { font-size: 28px; line-height: 1; color: var(--orange); }
  .toid { margin-top: 14px; font-size: 11px; letter-spacing: 3px; line-height: 1.2; font-weight: bold; }

  .tagline {
    position: absolute; left: 43px; top: 268px;
    font-family: "Oswald", sans-serif; font-weight: 600;
    font-size: 48px; color: var(--tagline); letter-spacing: -0.5px;
  }

  .photo { position: absolute; }
  .photo.inhaler { left: 0; top: 334px; width: 294px; height: 197px; background: linear-gradient(135deg, #9aa4ac, #d8c2ae); }
  .photo.classroom { left: 0; top: 535px; width: 294px; height: 198px; background: linear-gradient(180deg, #e6e1da, #b9875f); }
  .photo.bandage { left: 298px; top: 334px; width: 274px; height: 399px; background: linear-gradient(160deg, #7a5a3e, #e9c9b0 55%, #2c2a2a); }
  .photo.play { left: 576px; top: 334px; width: 294px; height: 198px; background: linear-gradient(160deg, #f0704f, #e25e4a 60%, #d9a0a8); }
  .photo.cpr { left: 576px; top: 536px; width: 294px; height: 197px; background: linear-gradient(135deg, #3b3434, #e5c7b3 55%, #c9a28e); }

  .courses-tab { position: absolute; left: 29px; top: 716px; width: 207px; height: 45px; }
  .courses-tab span {
    position: absolute; left: 0; top: 0; width: 100%; text-align: center;
    font-family: "Alfa Slab One", serif; font-size: 29px; color: #fff; line-height: 46px;
  }

  .course-list { position: absolute; left: 42px; top: 776px; list-style: none; font-size: 16.5px; line-height: 29px; letter-spacing: 0.3px; }

  .gift-card {
    position: absolute; left: 677px; top: 784px; width: 165px; height: 138px;
    border: 4px solid #fff; border-radius: 10px;
    box-shadow: 0 0 0 1px #d9d9d9, 0 2px 6px rgba(0,0,0,.25);
    background: radial-gradient(ellipse 120% 70% at 50% 0%, var(--light-orange) 60%, var(--orange) 61%);
    color: #fff; text-align: center; font-family: "Roboto", sans-serif; font-weight: 700;
  }
  .gift-amount { font-size: 48px; line-height: 1; margin-top: 10px; }
  .gift-label { font-size: 21px; line-height: 1.3; margin-top: 4px; }

  .coupon {
    position: absolute; left: 63px; top: 962px; width: 164px; height: 140px;
    background: var(--yellow); border: 4px dashed var(--red-orange); border-radius: 8px;
    box-shadow: 0 1px 4px rgba(0,0,0,.3);
    text-align: center; font-family: "Oswald", sans-serif; color: #fff;
  }
  .coupon-big { font-size: 36px; font-weight: 600; line-height: 1; margin-top: 16px; letter-spacing: -0.5px; }
  .coupon-small { font-size: 18px; font-weight: 500; line-height: 1.35; margin-top: 12px; }

  .benefit {
    position: absolute; left: 279px; width: 591px;
    color: #fff; text-align: right; padding-right: 18px;
    font-size: 16.5px; line-height: 20px;
    display: flex; align-items: center; justify-content: flex-end;
  }
  .benefit.one { top: 958px; height: 46px; background: var(--red-orange); }
  .benefit.two { top: 1007px; height: 47px; background: var(--deep-orange); }
  .benefit.three { top: 1057px; height: 47px; background: var(--yellow); line-height: 18px; }

  .call {
    position: absolute; left: 0; top: 1114px; width: 870px; text-align: center;
    font-family: "Roboto", sans-serif; font-weight: 700; font-size: 42px; color: var(--red-orange); word-spacing: 6px;
  }
  .contact {
    position: absolute; top: 1170px; font-family: "Roboto", sans-serif; font-weight: 700;
    font-size: 18px; color: var(--red-orange);
    transform: scaleX(0.9); transform-origin: left; white-space: nowrap;
  }
  .contact.web { left: 77px; }
  .contact.mail { left: 449px; }
</style>
</head>
<body>
  <main class="flyer">
    <div class="title-art" role="img" aria-label="Colourful wooden alphabet blocks spelling Child Care"></div>

    <div class="brand">
      <div class="brand-dot"></div>
      <div class="brand-name">crestwell learning</div>
      <div class="toid">TOID<br>47318</div>
    </div>

    <p class="tagline">making YOU the future of health care</p>

    <div class="photo inhaler" role="img" aria-label="Photo of a toddler using an asthma inhaler"></div>
    <div class="photo classroom" role="img" aria-label="Photo of two educators with a group of children at a classroom table"></div>
    <div class="photo bandage" role="img" aria-label="Photo of a carer applying a bandage to a young girl's knee"></div>
    <div class="photo play" role="img" aria-label="Photo of cheerful children with raised arms in a play room"></div>
    <div class="photo cpr" role="img" aria-label="Photo of gloved hands practising CPR on an infant manikin"></div>

    <div class="courses-tab">
      <svg width="207" height="45" viewBox="0 0 207 45" aria-hidden="true">
        <path d="M0 0 H207 L196 42 Q195 45 190 45 H17 Q12 45 11 42 Z" fill="var(--orange)"/>
      </svg>
      <span>COURSES</span>
    </div>

    <ul class="course-list">
      <li>HLTAID003 Provide First Aid</li>
      <li>HLTAID001 Provide Cardiopulmonary Resuscitation (CPR)</li>
      <li>22099VIC Course in First Aid Management of Anaphylaxis</li>
      <li>22024VIC Course in emergency management of asthma in the workplace</li>
      <li>HLTAID004 Provide an emergency first aid response in an<br>education and care setting</li>
    </ul>

    <div class="gift-card">
      <div class="gift-amount">$50</div>
      <div class="gift-label">VOLM<br>Gift Card</div>
    </div>

    <div class="coupon">
      <div class="coupon-big">50% OFF</div>
      <div class="coupon-small">Your Second<br>Training Session</div>
    </div>

    <p class="benefit one">We provide flexible, cost effective and reliable service</p>
    <p class="benefit two">We have training locations available in Blackburn, Preston, Narre<br>Warren and Mornington and can also provide onsite training</p>
    <p class="benefit three">We can also provide education and PRIVOS regulation<br>consultation to the childcare provider</p>

    <p class="call">Call (03) 5127 6481</p>
    <p class="contact web">website: www.crestwelllearning.com.au</p>
    <p class="contact mail">email: marapenn@crestwelllearning.com.au</p>
  </main>
</body>
</html>
```